Dalwin Electric Supply, Inc. Business Card Design

We are an Electrical Distributor looking for a Modern, Professional Business Card design.

Target Market(s)

Residential Commercial Industrial

Industry/Entity Type

Electrical

Contact Information for Business Card

Dalwin Electric Supply, Inc.
418 Tallow Creek Road
Brennick, NC 27514
555-312-4867
555-312-4921 Fax
dalwinelectric@voltmail.example

```html
<!DOCTYPE html>
<html lang="en">
<head>
<meta charset="utf-8">
<title>Dalwin Electric Supply, Inc. — Business Card</title>
<link rel="stylesheet" href="https://fonts.googleapis.com/css2?family=PT+Sans:wght@400;700&display=swap">
<style>
  :root {
    --backdrop: #e6e7e9;
    --card: #ffffff;
    --navy: #23239a;
    --rule: #5a5aa8;
    --shadow: rgba(40, 44, 56, 0.18);
  }
  * { box-sizing: border-box; margin: 0; padding: 0; }
  html, body {
    width: 1200px;
    height: 800px;
    overflow: hidden;
    background: var(--backdrop);
  }
  .canvas {
    position: relative;
    width: 1200px;
    height: 800px;
    display: flex;
    align-items: center;
    justify-content: center;
  }
  .business-card {
    position: relative;
    width: 840px;
    height: 480px;
    background: var(--card);
    box-shadow: 0 12px 36px var(--shadow);
    font-family: "PT Sans", Tahoma, sans-serif;
    color: var(--navy);
  }
  .brand {
    position: absolute;
    top: 46px;
    left: 50px;
    font-weight: 700;
    color: var(--navy);
    line-height: 1.05;
  }
  .brand-name {
    font-size: 48px;
    letter-spacing: -0.5px;
  }
  .brand-suffix {
    font-size: 48px;
  }
  .contact {
    position: absolute;
    right: 48px;
    bottom: 42px;
    text-align: right;
    font-size: 21px;
    line-height: 1.35;
  }
  .contact-line { display: block; }
  .contact-rule {
    border: none;
    border-top: 1.5px solid var(--rule);
    margin: 4px 0 3px auto;
    width: 100%;
  }
</style>
</head>
<body>
  <main class="canvas">
    <section class="business-card" aria-label="Business card front">
      <header class="brand">
        <div class="brand-name">Dalwin</div>
        <div class="brand-name">Electric Supply, Inc.</div>
      </header>
      <address class="contact" style="font-style:normal">
        <span class="contact-line">T: 555-312-4867</span>
        <span class="contact-line">F: 555-312-4921</span>
        <span class="contact-line">E: dalwinelectric@voltmail.example</span>
        <hr class="contact-rule">
        <span class="contact-line">418 Tallow Creek Road, Brennick, NC 27514</span>
      </address>
    </section>
  </main>
</body>
</html>
```